Stories Kept Close trifold brochure design

We are a start up company that will help seniors write their memoirs...beginning with a few ancestors and their heritage and continuing through their own history...how they would like to be remembered in the next generation. I envision a senior citizen at an older writing desk, writing her memoirs, with a book (maybe standing on top, leaning slightly) that has the words Stories Kept Close.com on the back binding. OR maybe a senior couple walking into the sunset with the same book somewhere in the frame. Communicating the relevance of every life being significant to those that come after them...when a genealogy doesn't say enough about the details of one's life. Please note that I am open to the professionals own ideas...I am not locked into my concepts. I would like one or two phrases..."When A Genealogy Doesn't Say Enough" and/or "Every life legacy is a gift for the next generation to treasure" to be in the design.
A few documents are loaded that contain notes for our web designers. Maybe they will help you with our thoughts.

Reason: We have added some additional photos that might be useful.

Target Market(s)

Seniors and the baby boomer generation

Industry/Entity Type

Graphic Design

Requirements
Must have
• Stories Kept Close
• Doris Whitlock, M.A.
• 1-717-555-0162 (local)
• 1-844-5TALES2 (toll free)
• info@storieskeptclose.example
• storieskeptclose.example
Should not have
• Scripts that would be challenging for seniors to read.

```html
<!DOCTYPE html>
<html lang="en">
<head>
<meta charset="utf-8">
<title>Stories Kept Close – Brochure Inside</title>
<link href="https://fonts.googleapis.com/css2?family=Merriweather:ital,wght@0,400;0,700;1,400;1,700&family=Mukta:wght@400;600;700&display=swap" rel="stylesheet">
<style>
  :root{
    --page:#e9e9e9;
    --paper:#ffffff;
    --panel-left:#ece8e1;
    --ink:#3f2c22;
    --ink-soft:#5a463a;
    --gold:#b39a5c;
    --gold-soft:#c9b27a;
    --gold-text:#8c7440;
    --card:#f4f1e6;
  }
  *{box-sizing:border-box;margin:0;padding:0}
  html,body{width:1200px;height:900px;overflow:hidden;background:var(--page)}
  body{position:relative;font-family:"Mukta",sans-serif;color:var(--ink)}
  .brochure{position:absolute;left:60px;top:40px;width:1080px;height:820px;background:var(--paper);box-shadow:0 6px 24px rgba(0,0,0,.18);overflow:hidden}
  .panel{position:absolute;top:0;height:100%}
  .panel-intro{left:0;width:360px;background:var(--panel-left);padding:28px 28px 0 32px;font-family:"Merriweather",serif}
  .panel-packages{left:360px;width:360px;padding:36px 20px 0 24px}
  .panel-contact{left:720px;width:360px}

  /* intro panel */
  .intro-headline{position:relative;height:112px;margin:0 -8px 12px 0}
  .headline-wash{position:absolute;inset:8px 0 6px 10px;background:#fbfaf7;border-radius:40px 8px 40px 8px;transform:rotate(-3deg)}
  .intro-headline p{position:relative;font-style:italic;font-weight:700;color:var(--gold-text);transform:rotate(-6deg);text-align:right;line-height:1.25;padding:20px 14px 0 0;font-size:14px}
  .intro-headline .big{font-size:22px;font-weight:400}
  .intro-lead{font-size:15.5px;font-weight:700;line-height:1.4;margin-bottom:12px}
  .intro-text{font-size:12.5px;line-height:1.38;color:var(--ink-soft);text-align:justify;margin-bottom:12px}
  .intro-sub{font-size:14px;font-style:italic;font-weight:700;margin-bottom:6px}

  /* packages panel */
  .section-title{font-family:"Merriweather",serif;font-style:italic;font-weight:700;font-size:22px}
  .section-title em{font-weight:400}
  .title-rule{height:3px;width:240px;background:linear-gradient(90deg,var(--gold),rgba(179,154,92,0));margin:4px 0 18px -4px;border-radius:2px}
  .step-title{font-family:"Merriweather",serif;font-weight:700;font-size:16px;margin-bottom:8px}
  .option{display:flex;gap:10px;align-items:flex-start;margin-bottom:12px;font-size:15px;line-height:1.25}
  .badge{flex:0 0 30px;height:30px;border-radius:50%;background:var(--gold);color:#fff;font-weight:600;font-size:19px;display:flex;align-items:center;justify-content:center}
  .package-label{font-family:"Merriweather",serif;color:var(--gold);font-size:16px;margin-top:6px}
  .package{background:var(--card);border-radius:12px;padding:6px 12px 8px 0;margin-left:-4px;width:325px}
  .package-head{display:flex;align-items:center;gap:10px;font-size:20px;font-weight:600;margin-left:-2px}
  .package-body{display:flex;gap:14px;margin-top:2px;padding-left:8px}
  .book{flex:0 0 96px;height:62px;border-radius:3px}
  .book-blue{background:linear-gradient(135deg,#dde9f2,#b9d3e6)}
  .book-lilac{background:linear-gradient(135deg,#eee4f2,#cfb7dc)}
  .book-peach{background:linear-gradient(135deg,#fbeadb,#f1c49c)}
  .package ul{list-style:disc;padding-left:18px;font-size:13.5px;line-height:1.25}

  /* contact panel */
  .tagline{position:absolute;left:-40px;top:34px;width:230px;text-align:center;font-family:"Merriweather",serif;font-style:italic;font-size:15px;color:var(--gold-text);line-height:1.3}
  .photo{position:absolute;border-radius:50%}
  .photo-hands{left:180px;top:-8px;width:176px;height:176px;background:radial-gradient(circle at 40% 60%,#e7b89c,#8fa7b8 70%)}
  .photo-writer{left:40px;top:140px;width:175px;height:175px;background:radial-gradient(circle at 50% 55%,#e9c9b0,#9c4e2e 75%)}
  .photo-sunset{left:200px;top:210px;width:160px;height:160px;background:radial-gradient(circle at 40% 30%,#f6e2a4,#c49338 55%,#3b2a18)}
  .notes{position:absolute;left:48px;top:410px;width:280px;list-style:none;font-size:15px;line-height:1.3}
  .notes li{position:relative;padding-left:22px;margin-bottom:20px}
  .notes li.arrow::before{content:"";position:absolute;left:0;top:4px;border-left:11px solid var(--gold);border-top:7px solid transparent;border-bottom:7px solid transparent}
  .notes li.star::before{content:"★";position:absolute;left:0;top:-2px;color:var(--gold);font-size:15px}
  .contact-card{background:var(--card);border-radius:12px;padding:10px 14px;font-size:15px;line-height:1.5;width:250px}
  .brand{position:absolute;left:140px;top:740px;display:flex;align-items:center;gap:8px;font-family:"Merriweather",serif;font-size:18px;color:var(--gold)}
  .brand-dot{width:12px;height:12px;border-radius:50%;background:var(--gold-soft)}
</style>
</head>
<body>
<div class="brochure">

  <section class="panel panel-intro">
    <div class="intro-headline">
      <div class="headline-wash"></div>
      <p>If you were alive in <span class="big">100 years,</span><br>what would you share with your<br><span class="big">descendants?</span></p>
    </div>
    <h2 class="intro-lead">Now you have a vehicle to help you <em>immortalize</em> your thoughts for the future…specifically for those who will want to know!</h2>
    <p class="intro-text">We are not all presidents of countries or CEO’s of fortune 500 companies! But “every life legacy is a gift to be treasured by the next generation.”</p>
    <p class="intro-text">Does your family host generations of soldiers, doctors, farmers, scientists, mechanics, entrepreneurs, writers, politicians, contractors, pastors, artisans, athletes, musicians, etc..? Generational patterns can often emerge when writing your story that will interest the next generation.</p>
    <h3 class="intro-sub">When a genealogy isn’t enough!</h3>
    <p class="intro-text">A genealogy, while very relevant, doesn’t offer the personal story of the names we find. A biography can place a deeper relevance on the face for future descendants. Every life is a legacy to pass forward and we at Stories Kept Close believe everyone should chronicle their life journey in writing. This commitment allows you to be remembered for who you truly are as a person.</p>
    <p class="intro-text">Think about it…Do you know the triumphs and tribulations of your ancestors? Do you wish you did? Well, so will those falling into your personal family tree.</p>
  </section>

  <section class="panel panel-packages">
    <h2 class="section-title">How we can <em>help</em></h2>
    <div class="title-rule"></div>
    <h3 class="step-title">First, choose an option:</h3>
    <div class="option"><span class="badge">A</span><p>You can provide the majority of input in an organized fashion (as specified by Stories Kept Close), OR</p></div>
    <div class="option"><span class="badge">B</span><p>We help organize photos and interview one-on-one for history, OR</p></div>
    <div class="option"><span class="badge">C</span><p>Bring friends together for a 12 week program so we can help you on your way.</p></div>
    <h3 class="step-title">Next, choose a package:</h3>

    <p class="package-label">Package</p>
    <div class="package">
      <div class="package-head"><span class="badge">1</span>Standard Portrait Book</div>
      <div class="package-body">
        <div class="book book-blue" role="img" aria-label="Open book icon with photo and text layout"></div>
        <ul><li>Up to 120 pages</li><li>8” x 10”</li><li>Include photos and text throughout</li></ul>
      </div>
    </div>

    <p class="package-label">Package</p>
    <div class="package">
      <div class="package-head"><span class="badge">2</span>Standard Trade Book</div>
      <div class="package-body">
        <div class="book book-lilac" role="img" aria-label="Open book icon with mostly text layout"></div>
        <ul><li>Up to 250 pages, or 100,000 words</li><li>6” x 9”</li><li>Few photos, mainly text</li></ul>
      </div>
    </div>

    <p class="package-label">Package</p>
    <div class="package">
      <div class="package-head"><span class="badge">3</span>Standard Portrait Book</div>
      <div class="package-body">
        <div class="book book-peach" role="img" aria-label="Open book icon with photo and text layout"></div>
        <ul><li>with 120 to 200 pages</li><li>8” x 10”</li><li>Include photos and text throughout</li></ul>
      </div>
    </div>
  </section>

  <section class="panel panel-contact">
    <p class="tagline">We offer several unique packages to best suit your needs.</p>
    <div class="photo photo-hands" role="img" aria-label="Photo of joined hands wearing wedding rings"></div>
    <div class="photo photo-writer" role="img" aria-label="Photo of a senior woman writing at an old wooden desk"></div>
    <div class="photo photo-sunset" role="img" aria-label="Photo of a child silhouetted against a golden sunset"></div>
    <ul class="notes">
      <li class="arrow">All publications will also be available as an <strong>ebook.</strong></li>
      <li class="arrow">Call or email us to schedule a <strong>free consultation</strong> individually or as a group today.</li>
      <li><div class="contact-card">1-717-555-0162<br>info@storieskeptclose.example</div></li>
      <li class="star">Ask about <strong>available financing</strong> if needed. We are committed to your legacy!</li>
    </ul>
    <div class="brand"><span class="brand-dot"></span>Stories Kept Close</div>
  </section>

</div>
</body>
</html>
```